Let's help people Kestrel with better hearing!

I need a business card for my private practice. I am a Dr. of Audiology and focus on hearing and tinnitus (ringing in the ears) treatment. My practice is named "Kestrel Hearing and Tinnitus Solutions". I want to communicate the idea of improved quality of life utilizing a natural color pallet Love the color turquoise as an accent. Want a professional look, while eye catching. I'm open to nontraditional design aesthetic. Something to get excited about and motivate people to improve their lives!

```html
<!DOCTYPE html>
<html lang="en">
<head>
<meta charset="utf-8">
<title>Kestrel Hearing and Tinnitus Solutions – Business Card</title>
<link rel="stylesheet" href="https://fonts.googleapis.com/css2?family=Questrial&family=Open+Sans:wght@400;600&display=swap">
<style>
  :root {
    --ink: #1f1f1f;
    --paper: #ffffff;
    --teal: #1fa596;
    --rule: #8a8a8a;
    --backdrop: #ecebe8;
    --light-text: #f2f2f2;
  }
  * { box-sizing: border-box; margin: 0; padding: 0; }
  html, body { width: 1200px; height: 784px; overflow: hidden; }
  body {
    background: var(--backdrop);
    font-family: "Open Sans", Arial, sans-serif;
    display: flex; flex-direction: column; align-items: center; justify-content: center;
    gap: 30px;
  }
  .card {
    position: relative;
    width: 620px; height: 354px;
    overflow: hidden;
    box-shadow: 0 6px 18px rgba(0,0,0,.18);
  }
  .card-back { background: var(--ink); }
  .card-front { background: var(--paper); }
  .card-art { position: absolute; inset: 0; width: 100%; height: 100%; }

  .wordmark {
    position: absolute;
    font-family: "Questrial", sans-serif;
    text-align: center;
  }
  .wordmark-name {
    font-size: 60px; line-height: 1; letter-spacing: 1px;
    padding-bottom: 8px;
  }
  .wordmark-tagline {
    font-size: 19px; line-height: 1.1; letter-spacing: .5px;
    text-transform: uppercase;
    border-top: 1px solid currentColor;
    border-bottom: 1px solid currentColor;
    padding: 6px 14px 12px;
  }
  .card-back .wordmark { left: 140px; top: 60px; width: 250px; color: var(--teal); }
  .card-front .wordmark { left: 70px; top: 78px; width: 250px; color: var(--ink); }
  .card-front .wordmark-tagline { border-color: var(--rule); }

  .person {
    position: absolute; right: 262px; top: 258px;
    text-align: right;
  }
  .person-name { color: var(--teal); font-weight: 600; font-size: 16px; line-height: 1.2; }
  .person-role { color: var(--light-text); font-size: 11px; }

  .contact-divider {
    position: absolute; left: 370px; top: 236px;
    width: 1px; height: 74px; background: var(--rule);
  }
  .contact-list {
    position: absolute; left: 382px; top: 234px;
    list-style: none;
    color: var(--light-text); font-size: 11.5px; line-height: 19px;
  }
  .contact-list li { display: flex; align-items: center; gap: 6px; white-space: nowrap; }
  .contact-icon { width: 13px; height: 13px; flex: none; }
</style>
</head>
<body>

  <section class="card card-back" aria-label="Card back">
    <div class="wordmark">
      <div class="wordmark-name">Kestrel</div>
      <div class="wordmark-tagline">Hearing &amp; Tinnitus<br>Solutions</div>
    </div>
  </section>

  <section class="card card-front" aria-label="Card front">
    <svg class="card-art" viewBox="0 0 620 354" aria-hidden="true">
      <path d="M0,354 L0,322 C190,300 400,230 540,90 C575,55 600,22 620,0 L620,354 Z" fill="var(--ink)"/>
      <path d="M330,238 C450,190 545,120 596,0 L620,0 L620,6 C590,110 500,190 330,240 Z" fill="var(--teal)"/>
    </svg>

    <div class="wordmark">
      <div class="wordmark-name">Kestrel</div>
      <div class="wordmark-tagline">Hearing &amp; Tinnitus<br>Solutions</div>
    </div>

    <div class="person">
      <div class="person-name">Mara Quinlan</div>
      <div class="person-role">Manager</div>
    </div>

    <div class="contact-divider"></div>

    <ul class="contact-list">
      <li>
        <svg class="contact-icon" viewBox="0 0 16 16"><rect x="4" y="1" width="8" height="14" rx="1.5" fill="var(--teal)"/><rect x="5.5" y="3" width="5" height="8" fill="var(--ink)"/></svg>
        +64 155 0187
      </li>
      <li>
        <svg class="contact-icon" viewBox="0 0 16 16"><rect x="1" y="3" width="14" height="10" fill="var(--teal)"/><path d="M1,3 L8,9 L15,3" stroke="var(--ink)" stroke-width="1.4" fill="none"/></svg>
        info@kestrelhearing.com
      </li>
      <li>
        <svg class="contact-icon" viewBox="0 0 16 16"><path d="M1,8 L8,2 L15,8 L13,8 L13,14 L3,14 L3,8 Z" fill="var(--teal)"/><rect x="6.5" y="10" width="3" height="4" fill="var(--ink)"/></svg>
        14 Kea St, Harbourside, Wellmont 4072
      </li>
      <li>
        <svg class="contact-icon" viewBox="0 0 16 16"><circle cx="8" cy="8" r="6.5" fill="none" stroke="var(--teal)" stroke-width="1.4"/><ellipse cx="8" cy="8" rx="2.8" ry="6.5" fill="none" stroke="var(--teal)" stroke-width="1.2"/><path d="M1.5,8 H14.5" stroke="var(--teal)" stroke-width="1.2"/></svg>
        www.kestrelhearing.com
      </li>
    </ul>
  </section>

</body>
</html>
```